Life Coaching Business Card

Please check out my website at www.lorettavisbeck.com. Ideally I would like to use the same colors that I used on the site to match my business cards i.e: pink, green, teal, white
I want the final design to include a picture of me and also to be appealing and eye catching. For the picture I submitted, you can crop it smaller to just have my face (exclude my chest) showing.
Industry/Entity Type
Business
Contact Information for Business Card
Loretta Visbeck
Transformational Life Coach
web: www.lorettavisbeck.com
email: loretta@lorettavisbeck.com
Phone: 555-318-7042
Look and feel
Each slider illustrates characteristics of the customer's brand and the style your logo design should communicate.

```html
<!DOCTYPE html>
<html lang="en">
<head>
<meta charset="utf-8">
<title>Loretta Visbeck – Transformational Life Coach Business Card</title>
<link rel="stylesheet" href="https://fonts.googleapis.com/css2?family=Josefin+Slab:wght@400;600;700&display=swap">
<style>
  :root {
    --backdrop: #ecebea;
    --pink-light: #f38fc0;
    --pink-mid: #e4579a;
    --pink-deep: #d0246a;
    --pink-title: #ee6fae;
    --white: #ffffff;
    --photo-light: #d9d9d9;
    --photo-mid: #8a8a8a;
    --photo-dark: #2b2b2b;
  }
  html, body {
    margin: 0;
    padding: 0;
    width: 1200px;
    height: 913px;
    overflow: hidden;
    background: var(--backdrop);
    font-family: "Josefin Slab", serif;
  }
  .canvas {
    position: relative;
    width: 1200px;
    height: 913px;
  }
  .card {
    position: absolute;
    top: 302px;
    width: 540px;
    height: 309px;
    overflow: hidden;
    box-shadow: 0 6px 18px rgba(0,0,0,0.18);
  }
  .card--front { left: 40px; }
  .card--back {
    left: 620px;
    background: linear-gradient(170deg, var(--pink-light) 0%, var(--pink-mid) 55%, var(--pink-deep) 100%);
    color: var(--white);
  }
  .portrait {
    position: absolute;
    inset: 0;
    background:
      radial-gradient(ellipse at 32% 62%, var(--photo-light) 0%, var(--photo-mid) 38%, transparent 60%),
      linear-gradient(160deg, var(--photo-light) 0%, var(--photo-mid) 40%, var(--photo-dark) 100%);
  }
  .title {
    position: absolute;
    right: 34px;
    text-align: right;
    line-height: 1;
  }
  .title__kicker {
    display: block;
    font-size: 19px;
    font-weight: 400;
    letter-spacing: 0.5px;
    margin-right: 4px;
  }
  .title__main {
    display: block;
    font-weight: 400;
    letter-spacing: 1px;
  }
  .card--front .title { top: 30px; color: var(--pink-title); }
  .card--front .title__main { font-size: 42px; }
  .card--back .title { top: 42px; }
  .card--back .title__main { font-size: 50px; }
  .holder-name {
    position: absolute;
    left: 30px;
    top: 40px;
    font-size: 21px;
    font-weight: 700;
    letter-spacing: 0.5px;
  }
  .contact {
    position: absolute;
    left: 30px;
    bottom: 26px;
    margin: 0;
    padding: 0;
    list-style: none;
    font-size: 19px;
    line-height: 1.45;
    font-weight: 600;
  }
</style>
</head>
<body>
<main class="canvas">
  <section class="card card--front">
    <div class="portrait" role="img" aria-label="Black and white portrait photo of the life coach smiling, seated on a sofa"></div>
    <h2 class="title">
      <span class="title__kicker">Transformational</span>
      <span class="title__main">LIFE COACH</span>
    </h2>
  </section>

  <section class="card card--back">
    <div class="holder-name">Loretta Visbeck</div>
    <h2 class="title">
      <span class="title__kicker">Transformational</span>
      <span class="title__main">LIFE COACH</span>
    </h2>
    <ul class="contact">
      <li>Web: www.lorettavisbeck.com</li>
      <li>Email: loretta@lorettavisbeck.com</li>
      <li>Phone: 555-318-7042</li>
    </ul>
  </section>
</main>
</body>
</html>
```